Harlow Consulting, Business Cards for International Development Consultancy

I'm an independent consultant working in the international development sector. I work with small organisations in developing countries to help them develop their community based programs so that they can be internationally competitive. This means they need to work better with their own communities to deliver meaningful quality work and also improve the accountability of their work so that they can compete for international and domestic funding.

I like the idea of being a connector between community, local organisations and international best practice and back again (ie acknowledging that international best practice can learn a lot from community).

My surname is Harlow - so I'd like the logo to use the idea of web as a connector.

I work with people with sight impairments - would like my card to be useful for low vision (i.e. clear graphics, easy to read font) and no vision (i.e. brail).

Target Market(s)

international non-government organisations (i.e. corvane, lift the villages, brightpath aid), Blue Harbour Green Lantern, government (i.e. Australian Bureau of Overseas Partnerships, consulars), non government agencies,

Industry/Entity Type

Business

Contact Information for Business Card

International Development Consultant
Connecting International Development with Community

Mirela Harlow
Lead Consultant
Phone: +61 412 558127
Email: mharlow.consulting@quillmail.net

Font styles to use
Sans Serif

Colors
eaf1f7
85acd3
d3a5cc
0456a4
a64599
0255a3

Requirements
Nice to have
• brail
Should not have
• fancy fonts - needs to be easy to read.

```html
<!DOCTYPE html>
<html lang="en">
<head>
<meta charset="utf-8">
<title>Harlow Consulting — Business Cards</title>
<link rel="stylesheet" href="https://fonts.googleapis.com/css2?family=PT+Sans:wght@400;700&display=swap">
<style>
  :root {
    --bg: #eaf1f7;
    --purple: #a64599;
    --purple-light: #b862ab;
    --pink-soft: #d3a5cc;
    --blue: #0456a4;
    --blue-deep: #0255a3;
    --blue-light: #85acd3;
    --silver: #c9ccd3;
    --white: #ffffff;
  }
  * { box-sizing: border-box; margin: 0; padding: 0; }
  html, body {
    width: 1200px; height: 761px; overflow: hidden;
    background: var(--bg);
    font-family: "PT Sans", sans-serif;
  }
  .stage {
    position: relative; width: 1200px; height: 761px;
    display: flex; align-items: center; justify-content: center; gap: 60px;
  }
  .card {
    position: relative; width: 520px; height: 300px;
    border-radius: 22px; overflow: hidden;
    box-shadow: 0 6px 18px rgba(2, 85, 163, 0.18);
  }
  .card svg.card-shapes { position: absolute; inset: 0; }
  .card-front .tagline {
    position: absolute; top: 52px; right: 36px; width: 360px;
    color: var(--white); font-weight: 700; font-size: 16px; line-height: 1.35;
    text-align: center; letter-spacing: 0.2px;
  }
  .card-back .identity {
    position: absolute; left: 150px; top: 112px; color: var(--white);
  }
  .card-back .name { font-size: 32px; font-weight: 700; letter-spacing: 0.5px; }
  .card-back .role { font-size: 15px; margin-top: 4px; }
  .card-back .role .phone { font-size: 12px; }
  .card-back .email {
    position: absolute; right: 30px; top: 238px;
    color: var(--white); font-size: 12px;
  }
</style>
</head>
<body>
<main class="stage">

  <section class="card card-front" aria-label="Card front">
    <svg class="card-shapes" width="520" height="300" viewBox="0 0 520 300">
      <defs>
        <linearGradient id="frontPurple" x1="0" y1="0" x2="1" y2="1">
          <stop offset="0" stop-color="var(--purple-light)"/>
          <stop offset="1" stop-color="var(--purple)"/>
        </linearGradient>
        <linearGradient id="frontBlue" x1="0" y1="0" x2="1" y2="1">
          <stop offset="0" stop-color="var(--blue-deep)"/>
          <stop offset="1" stop-color="var(--blue)"/>
        </linearGradient>
      </defs>
      <rect width="520" height="300" fill="url(#frontBlue)"/>
      <path d="M0,0 H520 V135 C430,150 340,118 255,160 C170,202 90,232 0,218 Z" fill="url(#frontPurple)"/>
      <rect x="40" y="20" width="460" height="150" rx="40" fill="var(--pink-soft)" opacity="0.12"
            role="img" aria-label="Faint world map behind the tagline"/>
      <path d="M0,222 C90,236 170,206 255,164 C340,122 430,154 520,139" fill="none" stroke="var(--silver)" stroke-width="5"/>
      <path d="M0,226 C90,240 170,210 255,168 C340,126 430,158 520,143" fill="none" stroke="var(--blue-light)" stroke-width="1.5" opacity="0.7"/>
    </svg>
    <p class="tagline">International Development Consultant<br>Connecting International Development with Community</p>
  </section>

  <section class="card card-back" aria-label="Card back">
    <svg class="card-shapes" width="520" height="300" viewBox="0 0 520 300">
      <defs>
        <radialGradient id="backNet" cx="0.55" cy="0.4" r="0.8">
          <stop offset="0" stop-color="#2f6fc8"/>
          <stop offset="0.6" stop-color="var(--blue)"/>
          <stop offset="1" stop-color="#1a3f93"/>
        </radialGradient>
      </defs>
      <rect width="520" height="300" fill="url(#backNet)" role="img"
            aria-label="Blue connection web pattern background"/>
      <rect x="0" y="232" width="520" height="26" fill="var(--purple)"/>
      <rect x="0" y="258" width="520" height="4" fill="var(--silver)"/>
    </svg>
    <div class="identity">
      <h1 class="name">Mirela Harlow</h1>
      <p class="role">Lead Consultant <span class="phone">( +61 412 558127 )</span></p>
    </div>
    <p class="email">Email: mharlow.consulting@quillmail.net</p>
  </section>

</main>
</body>
</html>
```